Business Card Design

I am an child sleep consultant. I would like the picture to be the background of the card and for my logo to be in the upper right hand corner. Other than that, the design is yours!!

Business

Marta Kovel
Red Fern Slumber
Certified Child Sleep Consultant
(555) 286-9153
redfernslumber.com

```html
<!DOCTYPE html>
<html lang="en">
<head>
<meta charset="utf-8">
<title>Red Fern Slumber – Business Card</title>
<link href="https://fonts.googleapis.com/css2?family=Arimo:wght@400;500;700&display=swap" rel="stylesheet">
<style>
  :root {
    --photo-highlight: #ececec;
    --photo-light: #cfcfcf;
    --photo-mid: #a3a3a3;
    --photo-dark: #5c5c5c;
    --photo-deep: #3a3a3a;
    --panel-yellow: #f3f0a6;
    --panel-yellow-soft: #f8f6cc;
    --accent-teal: #7eecd2;
    --accent-teal-soft: #b9f2e2;
    --ink-dark: #2b2b2b;
    --ink-slate: #56616b;
  }
  html, body {
    margin: 0;
    padding: 0;
    overflow: hidden;
    background: #ffffff;
  }
  .card {
    position: relative;
    width: 1200px;
    height: 702px;
    overflow: hidden;
    font-family: "Arimo", Arial, sans-serif;
  }
  .background-photo {
    position: absolute;
    inset: 0;
    background:
      radial-gradient(ellipse 360px 420px at 330px 400px, var(--photo-highlight) 0%, rgba(236,236,236,0.6) 45%, rgba(236,236,236,0) 75%),
      radial-gradient(ellipse 260px 200px at 640px 120px, rgba(58,58,58,0.55) 0%, rgba(58,58,58,0) 100%),
      radial-gradient(ellipse 200px 300px at 30px 420px, rgba(92,92,92,0.45) 0%, rgba(92,92,92,0) 100%),
      linear-gradient(160deg, var(--photo-light) 0%, var(--photo-mid) 45%, var(--photo-dark) 85%, var(--photo-deep) 100%);
  }
  .info-panel {
    position: absolute;
    inset: 0;
  }
  .brand {
    position: absolute;
    left: 820px;
    top: 60px;
    width: 300px;
    display: flex;
    flex-direction: column;
    align-items: center;
    gap: 22px;
  }
  .brand-mark {
    width: 150px;
    height: 150px;
    border-radius: 50%;
    background: var(--accent-teal-soft);
  }
  .brand-name {
    margin: 0;
    font-weight: 700;
    font-size: 38px;
    line-height: 1.15;
    text-align: center;
    color: var(--ink-dark);
  }
  .website {
    position: absolute;
    left: 732px;
    top: 403px;
    margin: 0;
    font-size: 44px;
    line-height: 1;
    font-weight: 500;
    letter-spacing: 1.5px;
    color: var(--accent-teal);
  }
  .rule {
    position: absolute;
    height: 2px;
    background: var(--accent-teal);
  }
  .rule-website { left: 730px; top: 457px; width: 470px; }
  .rule-name { left: 909px; top: 523px; width: 291px; }
  .rule-phone { left: 1015px; top: 640px; width: 185px; }
  .person-name {
    position: absolute;
    left: 641px;
    top: 488px;
    margin: 0;
    font-size: 46px;
    line-height: 1;
    font-weight: 500;
    color: var(--ink-dark);
  }
  .job-title {
    position: absolute;
    left: 641px;
    top: 542px;
    margin: 0;
    font-size: 35px;
    line-height: 1;
    font-weight: 400;
    color: var(--ink-slate);
  }
  .phone {
    position: absolute;
    left: 636px;
    top: 606px;
    margin: 0;
    display: flex;
    align-items: center;
    gap: 14px;
    font-size: 46px;
    line-height: 1;
    font-weight: 500;
    color: var(--ink-dark);
  }
  .phone-icon { width: 44px; height: 44px; }
</style>
</head>
<body>
  <main class="card">
    <div class="background-photo" role="img" aria-label="Black and white close-up photograph of a smiling baby filling the card background"></div>

    <svg class="info-panel" width="1200" height="702" viewBox="0 0 1200 702" aria-hidden="true">
      <defs>
        <linearGradient id="panelTone" x1="0" y1="0" x2="1" y2="1">
          <stop offset="0" stop-color="#f8f6cc"/>
          <stop offset="1" stop-color="#f3f0a6"/>
        </linearGradient>
      </defs>
      <polygon points="783,0 1200,0 1200,702 553,702" fill="url(#panelTone)"/>
    </svg>

    <div class="brand">
      <div class="brand-mark"></div>
      <p class="brand-name">Red Fern Slumber</p>
    </div>

    <p class="website">redfernslumber.com</p>
    <div class="rule rule-website"></div>

    <h1 class="person-name">Marta Kovel</h1>
    <div class="rule rule-name"></div>
    <p class="job-title">Certified Child Sleep Consultant</p>

    <p class="phone">
      <svg class="phone-icon" viewBox="0 0 24 24" aria-hidden="true">
        <path fill="#7eecd2" d="M6.6 10.8c1.4 2.8 3.8 5.1 6.6 6.6l2.2-2.2c.3-.3.7-.4 1-.2 1.1.4 2.3.6 3.6.6.6 0 1 .4 1 1V20c0 .6-.4 1-1 1C10.6 21 3 13.4 3 4c0-.6.4-1 1-1h3.5c.6 0 1 .4 1 1 0 1.3.2 2.5.6 3.6.1.3 0 .7-.2 1l-2.3 2.2z"/>
      </svg>
      <span>(555) 286-9153</span>
    </p>
    <div class="rule rule-phone"></div>
  </main>
</body>
</html>
```